Paws Of Kindness Business cards

Design a cool, modern business card for my bully breed rescue.

Contact Information for Business Card

Marlene
517-382-4061 Marlene@PawsOfKindnessRescue.net PawsOfKindnessRescue.net

Font styles to use
Serif
Sans Serif

Colors

Designer to choose colors to be used in the design.

Requirements
Must have
• logo and info. Color
Nice to have
• Foil. Maybe some paw prints on the back or some kind of dog illustration.

```html
<!DOCTYPE html>
<html lang="en">
<head>
<meta charset="utf-8">
<title>Paws Of Kindness – Business Cards</title>
<link href="https://fonts.googleapis.com/css2?family=Roboto:wght@400;500;700;900&display=swap" rel="stylesheet">
<style>
  :root {
    --bg: #2a2a2a;
    --card-white: #ffffff;
    --brand-red: #e8232f;
    --brand-yellow: #f7c51c;
    --ink: #141414;
    --photo-warm: #8a6a52;
    --photo-dark: #4a3a30;
    --photo-haze: rgba(215, 212, 205, 0.62);
  }
  * { box-sizing: border-box; margin: 0; padding: 0; }
  html, body { width: 1200px; height: 930px; overflow: hidden; }
  body { background: var(--bg); font-family: "Roboto", Arial, sans-serif; position: relative; }

  .card {
    position: absolute;
    width: 640px;
    height: 366px;
    border-radius: 18px;
    overflow: hidden;
    box-shadow: 0 10px 28px rgba(0,0,0,0.45);
  }

  /* Back side */
  .card--back { left: 60px; top: 60px; }
  .card-back__photo {
    position: absolute; inset: 0;
    background: radial-gradient(ellipse at 38% 55%, var(--photo-warm) 0%, #6d5544 35%, var(--photo-dark) 70%, #5c4b3f 100%);
  }
  .card-back__haze { position: absolute; inset: 0; background: var(--photo-haze); }
  .brand-lockup {
    position: absolute;
    display: flex; align-items: center; gap: 12px;
    color: var(--ink);
  }
  .brand-lockup__dot {
    width: 24px; height: 24px; border-radius: 50%;
    background: var(--brand-red);
    flex: none;
  }
  .brand-lockup__name {
    font-weight: 900; font-size: 40px; letter-spacing: 0.5px; white-space: nowrap;
  }
  .card--back .brand-lockup { left: 50%; top: 50%; transform: translate(-50%, -50%); }

  /* Front side */
  .card--front { left: 500px; top: 504px; background: var(--card-white); }
  .card-front__waves { position: absolute; inset: 0; width: 100%; height: 100%; }
  .card--front .brand-lockup { left: 36px; top: 124px; }
  .card--front .brand-lockup__name { font-size: 28px; }

  .contact {
    position: absolute; right: 28px; top: 116px;
    text-align: right; color: var(--card-white);
  }
  .contact__name {
    font-size: 30px; font-weight: 500; color: var(--brand-yellow);
    text-transform: uppercase; letter-spacing: 0.5px; line-height: 1;
  }
  .contact__role { font-size: 16px; margin-top: 4px; margin-bottom: 18px; }
  .contact__list { list-style: none; }
  .contact__item {
    display: flex; justify-content: flex-end; align-items: center; gap: 10px;
    font-size: 14px; line-height: 25px; white-space: nowrap;
  }
  .contact__icon { width: 13px; height: 13px; flex: none; }
</style>
</head>
<body>

  <section class="card card--back" aria-label="Business card back">
    <div class="card-back__photo" role="img" aria-label="Faded photograph of a bully breed dog"></div>
    <div class="card-back__haze"></div>
    <div class="brand-lockup">
      <span class="brand-lockup__dot"></span>
      <span class="brand-lockup__name">Paws Of Kindness</span>
    </div>
  </section>

  <section class="card card--front" aria-label="Business card front">
    <svg class="card-front__waves" viewBox="0 0 640 366" preserveAspectRatio="none" aria-hidden="true">
      <path d="M0 300 C110 292 230 255 305 190 C235 265 120 312 0 318 Z" fill="var(--brand-yellow)"/>
      <path d="M0 324 C140 320 270 275 330 180 C295 265 190 330 60 366 L0 366 Z" fill="var(--brand-red)"/>
      <path d="M640 20 C510 6 405 46 352 150 C305 240 260 320 140 366 L640 366 Z" fill="var(--brand-red)"/>
      <path d="M640 36 C516 22 420 60 368 160 C322 248 280 326 170 366" fill="none" stroke="var(--card-white)" stroke-width="6"/>
    </svg>

    <div class="brand-lockup">
      <span class="brand-lockup__dot"></span>
      <span class="brand-lockup__name">Paws Of Kindness</span>
    </div>

    <div class="contact">
      <p class="contact__name">Marlene</p>
      <p class="contact__role">Director</p>
      <ul class="contact__list">
        <li class="contact__item">517-382-4061
          <svg class="contact__icon" viewBox="0 0 16 16" aria-hidden="true"><path d="M3 1h3l1.5 4-2 1.2a9 9 0 0 0 4.3 4.3L11 8.5l4 1.5v3a2 2 0 0 1-2 2A12 12 0 0 1 1 3a2 2 0 0 1 2-2z" fill="var(--brand-yellow)"/></svg>
        </li>
        <li class="contact__item">Marlene@PawsOfKindnessRescue.net
          <svg class="contact__icon" viewBox="0 0 16 16" aria-hidden="true"><rect x="1" y="3" width="14" height="10" rx="1" fill="none" stroke="var(--brand-yellow)" stroke-width="1.6"/><path d="M1.5 3.8 8 9l6.5-5.2" fill="none" stroke="var(--brand-yellow)" stroke-width="1.6"/></svg>
        </li>
        <li class="contact__item">www.PawsOfKindnessRescue.net
          <svg class="contact__icon" viewBox="0 0 16 16" aria-hidden="true"><circle cx="8" cy="8" r="7" fill="var(--brand-yellow)"/><path d="M1 8h14M8 1c-3 3-3 11 0 14M8 1c3 3 3 11 0 14" fill="none" stroke="var(--brand-red)" stroke-width="1"/></svg>
        </li>
      </ul>
    </div>
  </section>

</body>
</html>
```